French flying club (aeroclub) complete wordpress theme

We need a complete wordpress theme to overhaul the look and feel of our aeroclub website.

We are a flying club (aeroclub) based in France, near Paris. We are a non-profit organization providing VFR flight training to members of all ages; our instructors all have extensive experience flying professionally (one of them was captain on the Stratoline!) We have a fleet of 3 aircraft of the same type (Pelvo) that we provide to our members at competitive rates: since we are a non-profit, there are no unnecessary margins on what we charge aside from what’s necessary for renewal of a fun-to-fly fleet!

The club has a very old history (founded in 1950), and was initially founded by female pioneers of aviation in France (corps founded in 1934), serving as flying nurses for the French army in various conflicts and for search-and-rescue missions. Now of course we accept all types of applicants! Our members are genuinely passionate about flying, they care more about time airborne than about the glamour surrounding aviation (not that it does not matter).

We are launching this website design contest because our current website (http://www.aeroclub-kelvo.org/) is somewhat stuck in the ‘90s, and we’d like to give it a new look and feel.

Some designs that caught our attention, to draw inspiration from:
- http://www.volbrumeclub.fr/
- http://www.cieldutal.com/
- http://www.ecole-varnot.com/

Idea would be to provide front page access to the latest pictures and movies taken from our latest flights, a few breaking news, and one click access to a few sections, e.g.:
- our fleet/prices
- instruction options (VFR, night VFR, BIA etc.)
- location and contact info
- history
- a members-private login page for aircraft reservation and planning access, supporting some sort of forum/message board would etc.

When it comes to style, we’re looking for things that relate to our logo colors (blue dominant with some red and white). Our logo can be found at http://www.aeroclub-kelvo.org/images/banners_logos/logo_kelvo.gif (we can provide a higher resolution one upon request).

Attached are a few excerpts from existing pages (zip file). They're in French but content is usually self-explanatory. Explanations can be provided if necessary.

Target Market(s)

We tend to have various ‘segments’ of users:
- Teenagers and young adults looking to learn flying
- Seniors looking to learn flying
- Experienced pilots who are looking for a no-nonsense, flying enthusiast community

Industry/Entity Type

Club

Font styles to use
Sans Serif

Requirements
Must have
• Theme should be supplied as a self-deployable wordpress package that can be deployed on a fresh instance of wordpress (i.e. wordpress-compatible zip archive)

```html
<!DOCTYPE html>
<html lang="en">
<head>
<meta charset="utf-8">
<title>Aéroclub Kelvo</title>
<link rel="stylesheet" href="https://fonts.googleapis.com/css2?family=Open+Sans:wght@400;600;700&display=swap">
<style>
:root{
  --navy:#1f1c55;
  --blue:#1b76cf;
  --blue-dark:#145ea8;
  --red:#d8262e;
  --ink:#333;
  --muted:#666;
  --panel:#f1f1f1;
  --footer:#2b2e34;
  --footer-deep:#1f2125;
  --footer-text:#a7abb2;
  --white:#fff;
}
*{box-sizing:border-box;margin:0;padding:0}
html,body{width:783px;height:1200px;overflow:hidden}
body{font-family:"Open Sans",Arial,sans-serif;color:var(--ink);background:var(--white);position:relative;font-size:9px;line-height:1.45}
.wrap{position:absolute;left:78px;width:627px}

/* header */
.site-header{position:absolute;top:0;left:0;width:783px;height:73px;background:var(--white);z-index:3}
.brand{position:absolute;left:78px;top:6px;width:140px;height:130px;background:var(--white);border-radius:4px;box-shadow:0 2px 6px rgba(0,0,0,.15);display:flex;flex-direction:column;align-items:center;justify-content:center;gap:8px;z-index:4}
.brand-dot{width:54px;height:54px;border-radius:50%;background:var(--blue)}
.brand-name{font-weight:700;font-size:14px;color:var(--navy)}
.topbar{position:absolute;top:6px;right:78px;display:flex;align-items:center;gap:12px}
.login{background:var(--red);color:var(--white);font-size:9px;font-weight:600;padding:4px 10px;border-radius:2px}
.phone{display:flex;align-items:center;gap:5px;font-size:10px;color:var(--navy);font-weight:600}
.social{display:flex;gap:6px}
.social span{width:14px;height:14px;border-radius:50%;background:var(--blue)}
.nav{position:absolute;top:42px;right:78px;display:flex;list-style:none}
.nav li{font-size:9px;color:var(--navy);padding:8px 8px;font-weight:600;white-space:nowrap}
.nav li.active{background:#e4e6ea;border-top:2px solid var(--blue)}

/* hero */
.hero{position:absolute;top:73px;left:0;width:783px;height:279px;background:linear-gradient(180deg,#7fa6cf 0%,#b9cfe4 55%,#8d8f91 72%,#5f6164 100%)}
.arrow{position:absolute;top:125px;width:22px;height:22px;border-radius:50%;background:rgba(20,20,30,.75);display:flex;align-items:center;justify-content:center}
.arrow.prev{left:14px}.arrow.next{right:14px}

/* about */
.about{top:340px;height:90px;background:var(--navy);color:var(--white);padding:10px 14px}
.about h2{font-size:13px;font-weight:700;margin-bottom:6px;border-bottom:1px solid rgba(255,255,255,.25);padding-bottom:5px}
.about p{font-size:8.5px;color:#cfd0e6}

/* services */
.services{top:458px}
.section-title{font-size:14px;font-weight:600;color:var(--navy);margin-bottom:12px}
.service-grid{display:grid;grid-template-columns:repeat(4,1fr);gap:12px}
.service-photo{height:90px;border-radius:2px}
.service p{font-size:8px;color:var(--muted);margin-top:6px}

/* why choose */
.why-band{position:absolute;top:655px;left:0;width:783px;height:285px;background:var(--panel)}
.why{top:672px;width:470px}
.why h2{font-size:13px;font-weight:700;color:var(--navy);margin-bottom:10px}
.why p{font-size:8.5px;color:var(--muted);margin-bottom:10px}
.ticks{list-style:none}
.ticks li{display:flex;align-items:center;gap:7px;font-size:8.5px;color:var(--muted);margin-bottom:8px}
.news{position:absolute;top:672px;left:569px;width:136px;height:242px;background:var(--blue);color:var(--white);padding:10px}
.news h3{font-size:13px;font-weight:700;border-bottom:1px solid rgba(255,255,255,.35);padding-bottom:6px;margin-bottom:9px}
.news-item{display:flex;gap:6px;margin-bottom:11px}
.date{flex:none;width:24px;height:28px;background:var(--red);font-size:7px;font-weight:700;text-align:center;line-height:1.2;padding-top:4px}
.news-item p{font-size:7.5px;line-height:1.35}
.more{position:absolute;right:10px;bottom:8px;font-size:7.5px;font-weight:600}

/* footer */
.site-footer{position:absolute;top:940px;left:0;width:783px;height:260px;background:var(--footer);color:var(--footer-text)}
.site-footer h4{color:var(--white);font-size:10px;font-weight:600;margin-bottom:12px}
.fcol{position:absolute;top:32px}
.footer-brand{left:78px;width:120px;text-align:center}
.footer-mark{display:flex;flex-direction:column;align-items:center;gap:6px;margin-bottom:12px}
.footer-mark .brand-dot{width:44px;height:44px;background:#4a4e56}
.footer-mark span{color:var(--white);font-weight:700;font-size:11px}
.footer-brand p{font-size:7.5px;text-align:left}
.recent{left:232px;width:150px}
.post{display:flex;gap:7px;margin-bottom:12px}
.post-thumb{flex:none;width:26px;height:26px;border-radius:50%;background:linear-gradient(135deg,#7f96b3,#4d5a6b)}
.post p{font-size:7.5px}
.post b{display:block;color:#d7d9dd;font-weight:600}
.getsocial{left:400px;width:150px}
.fsocial{display:flex;gap:6px;margin-bottom:16px}
.fsocial span{width:16px;height:16px;border-radius:50%;background:#4a4e56}
.getsocial p{font-size:7.5px;margin-bottom:10px}
.subscribe{display:flex}
.subscribe input{width:92px;height:18px;border:0;font:7.5px "Open Sans",Arial,sans-serif;padding:0 5px}
.subscribe button{height:18px;border:0;background:var(--blue);color:var(--white);font:600 7.5px "Open Sans",Arial,sans-serif;padding:0 8px}
.contact{left:580px;width:125px}
.contact li{list-style:none;display:flex;gap:5px;align-items:center;font-size:7.5px;margin-bottom:5px}
.map{margin-top:8px;height:44px;background:linear-gradient(135deg,#d8d6cf,#b9c6b4)}
.bottom-bar{position:absolute;bottom:0;left:0;width:783px;height:22px;background:var(--footer-deep)}
</style>
</head>
<body>

<header class="site-header">
  <div class="brand"><span class="brand-dot"></span><span class="brand-name">Aéroclub Kelvo</span></div>
  <div class="topbar">
    <span class="login">Member Login</span>
    <span class="phone">
      <svg width="10" height="10" viewBox="0 0 24 24"><path fill="#1f1c55" d="M6.6 10.8a15 15 0 0 0 6.6 6.6l2.2-2.2a1 1 0 0 1 1-.25 11.4 11.4 0 0 0 3.6.57 1 1 0 0 1 1 1V20a1 1 0 0 1-1 1A17 17 0 0 1 3 4a1 1 0 0 1 1-1h3.5a1 1 0 0 1 1 1 11.4 11.4 0 0 0 .57 3.6 1 1 0 0 1-.25 1z"/></svg>
      +30 412 7789
    </span>
    <span class="social"><span></span><span></span><span></span></span>
  </div>
  <ul class="nav">
    <li class="active">Club Info</li><li>News</li><li>Events</li><li>Useful Info</li><li>Tradition</li><li>Contact</li><li>Reservation</li><li>Members</li>
  </ul>
</header>

<section class="hero" role="img" aria-label="Business jet parked on the apron under a clear sky">
  <span class="arrow prev"><svg width="8" height="10" viewBox="0 0 8 10"><path d="M6 1 2 5l4 4" stroke="#fff" stroke-width="2" fill="none"/></svg></span>
  <span class="arrow next"><svg width="8" height="10" viewBox="0 0 8 10"><path d="m2 1 4 4-4 4" stroke="#fff" stroke-width="2" fill="none"/></svg></span>
</section>

<section class="wrap about">
  <h2>About Us</h2>
  <p>Founded in 1950 by pioneering women aviators, our club offers VFR flight training to members of every age. Our instructors bring long professional careers to each lesson, and our fleet of three aircraft is shared at fair, non-profit rates so that more of your time is spent in the air and less on the ground.</p>
</section>

<section class="wrap services">
  <h2 class="section-title">Services we offer</h2>
  <div class="service-grid">
    <div class="service"><div class="service-photo" role="img" aria-label="Cockpit instrument panel" style="background:linear-gradient(135deg,#3b3f46,#8a8f96)"></div><p>simply dummy text of the printing and type setting industry. Lorem ipsum has been the industry's.</p></div>
    <div class="service"><div class="service-photo" role="img" aria-label="Light aircraft on the grass" style="background:linear-gradient(135deg,#9fc0e0,#6f8f5a)"></div><p>simply dummy text of the printing and type setting industry. Lorem ipsum has been the industry's.</p></div>
    <div class="service"><div class="service-photo" role="img" aria-label="Pilot training in the cockpit" style="background:linear-gradient(135deg,#2e3440,#7d6a58)"></div><p>simply dummy text of the printing and type setting industry. Lorem ipsum has been the industry's.</p></div>
    <div class="service"><div class="service-photo" role="img" aria-label="Aircraft engine under maintenance" style="background:linear-gradient(135deg,#c9cdd2,#8c3b34)"></div><p>simply dummy text of the printing and type setting industry. Lorem ipsum has been the industry's.</p></div>
  </div>
</section>

<div class="why-band"></div>
<section class="wrap why">
  <h2>Why Choose Us ?</h2>
  <p>Come to the Aero Club of Kelvo to share the passion of an aviation tradition of flying club, based at Marvelle-sur-Orge (West of Paris).</p>
  <p>Lorem Ipsum is simply dummy text of the printing and typesetting industry. Lorem Ipsum has been the industry's standard dummy text ever since the 1500s, when an unknown printer took a galley of type and scrambled it to make a type specimen book.</p>
  <ul class="ticks">
    <li><svg width="9" height="9" viewBox="0 0 10 10"><circle cx="5" cy="5" r="5" fill="#1f1c55"/><path d="m3 5 1.5 1.5L7 3.5" stroke="#fff" stroke-width="1.2" fill="none"/></svg>Lorem Ipsum has been the industry's standard dummy text.</li>
    <li><svg width="9" height="9" viewBox="0 0 10 10"><circle cx="5" cy="5" r="5" fill="#1f1c55"/><path d="m3 5 1.5 1.5L7 3.5" stroke="#fff" stroke-width="1.2" fill="none"/></svg>Lorem standard dummy text ever since the 1500s, when an unknown printer.</li>
    <li><svg width="9" height="9" viewBox="0 0 10 10"><circle cx="5" cy="5" r="5" fill="#1f1c55"/><path d="m3 5 1.5 1.5L7 3.5" stroke="#fff" stroke-width="1.2" fill="none"/></svg>Standard dummy text ever since the 1500s, when an unknown printer industry's standard.</li>
    <li><svg width="9" height="9" viewBox="0 0 10 10"><circle cx="5" cy="5" r="5" fill="#1f1c55"/><path d="m3 5 1.5 1.5L7 3.5" stroke="#fff" stroke-width="1.2" fill="none"/></svg>Lorem Ipsum has been the industry's when an unknown printer took a galley.</li>
    <li><svg width="9" height="9" viewBox="0 0 10 10"><circle cx="5" cy="5" r="5" fill="#1f1c55"/><path d="m3 5 1.5 1.5L7 3.5" stroke="#fff" stroke-width="1.2" fill="none"/></svg>Lorem Ipsum has been the when an unknown printer took a galley.</li>
  </ul>
</section>

<aside class="news">
  <h3>Latest News</h3>
  <div class="news-item"><span class="date">10<br>May</span><p>Lorem Ipsum has been the industry's standard dummy text ever.</p></div>
  <div class="news-item"><span class="date">10<br>May</span><p>Lorem Ipsum has been the industry's standard dummy text ever. The industry's standard.</p></div>
  <div class="news-item"><span class="date">10<br>May</span><p>Lorem Ipsum has been the industry's standard dummy text ever.</p></div>
  <span class="more">Read More »</span>
</aside>

<footer class="site-footer">
  <div class="fcol footer-brand">
    <div class="footer-mark"><span class="brand-dot"></span><span>Aéroclub Kelvo</span></div>
    <p>Flying club founded in 1950, offering VFR training and a friendly community of passionate pilots near Paris.</p>
  </div>
  <div class="fcol recent">
    <h4>Recent Post</h4>
    <div class="post"><span class="post-thumb" role="img" aria-label="Post thumbnail"></span><p><b>First solo flight of the spring</b>Posted 12 May</p></div>
    <div class="post"><span class="post-thumb" role="img" aria-label="Post thumbnail"></span><p><b>Night VFR course opens soon</b>Posted 08 May</p></div>
  </div>
  <div class="fcol getsocial">
    <h4>Get Social</h4>
    <div class="fsocial"><span></span><span></span><span></span><span></span></div>
    <h4>Newsletter</h4>
    <p>Receive club news, events and flight reports directly in your inbox.</p>
    <div class="subscribe"><input type="text" value="Email Address" aria-label="Email address"><button>Subscribe</button></div>
  </div>
  <div class="fcol contact">
    <h4>Contact Details</h4>
    <ul>
      <li><svg width="8" height="8" viewBox="0 0 24 24"><path fill="#a7abb2" d="M6.6 10.8a15 15 0 0 0 6.6 6.6l2.2-2.2a1 1 0 0 1 1-.25 11.4 11.4 0 0 0 3.6.57 1 1 0 0 1 1 1V20a1 1 0 0 1-1 1A17 17 0 0 1 3 4a1 1 0 0 1 1-1h3.5a1 1 0 0 1 1 1 11.4 11.4 0 0 0 .57 3.6 1 1 0 0 1-.25 1z"/></svg>+30 412 7789</li>
      <li><svg width="8" height="8" viewBox="0 0 24 24"><rect x="2" y="5" width="20" height="14" fill="none" stroke="#a7abb2" stroke-width="2"/><path d="m2 5 10 8 10-8" fill="none" stroke="#a7abb2" stroke-width="2"/></svg>contact@aeroclub-kelvo.org</li>
      <li><svg width="8" height="8" viewBox="0 0 24 24"><path fill="#a7abb2" d="M12 2a7 7 0 0 0-7 7c0 5 7 13 7 13s7-8 7-13a7 7 0 0 0-7-7zm0 9.5A2.5 2.5 0 1 1 12 6.5a2.5 2.5 0 0 1 0 5z"/></svg>Hangar 4, Aérodrome Ouest</li>
    </ul>
    <div class="map" role="img" aria-label="Map of the airfield location"></div>
  </div>
  <div class="bottom-bar"></div>
</footer>

</body>
</html>
```